Ridgecrest Casino poster and artwork for the 48th Falcon Crown Stakes

Ridgecrest Casino hosts the Falcon Crown Stakes each year. The derby purse is $750,000 and we are Grade III this year. The derby date is August 5, 2017 with the post time at 2pm.

Once the artwork is selected we will use it for posters, invites, e-blasts, website etc.

I have attached the artwork from 2016 as an example. The logo must be included in the artwork and it is also attached

Industry/Entity Type

Casino

Font styles to use
Sans Serif

Requirements
Must have
• Falcon Crown logo (attached)
• Date-August 5, 2017
• First post time at 2pm
• Ridgecrest Casino (logo attached)

```html
<!DOCTYPE html>
<html lang="en">
<head>
<meta charset="utf-8">
<title>Falcon Crown Stakes – Ridgecrest Casino</title>
<link rel="stylesheet" href="https://fonts.googleapis.com/css2?family=Libre+Bodoni:wght@400;700&display=swap">
<style>
  :root {
    --backdrop: #ecebe8;
    --sky: #93b6cf;
    --sky-deep: #5f87a6;
    --haze: #a9b7b8;
    --dirt: #c98a3e;
    --dirt-deep: #5e4330;
    --silks: #2f7a4c;
    --silks-deep: #1f4f35;
    --bay: #3a2a22;
    --text-light: #ffffff;
    --text-shadow: rgba(20, 20, 20, 0.55);
  }
  * { margin: 0; padding: 0; box-sizing: border-box; }
  html, body {
    width: 1200px;
    height: 900px;
    overflow: hidden;
    background: var(--backdrop);
  }
  .poster {
    position: absolute;
    left: 300px;
    top: 28px;
    width: 600px;
    height: 844px;
    overflow: hidden;
    font-family: "Libre Bodoni", "Bodoni Moda", serif;
    color: var(--text-light);
    box-shadow: 0 6px 18px rgba(0,0,0,0.25);
  }
  .track-backdrop {
    position: absolute;
    inset: 0;
    background: linear-gradient(180deg, var(--sky-deep) 0%, var(--sky) 28%, var(--haze) 58%, var(--dirt) 82%, var(--dirt-deep) 100%);
  }
  .race-photo {
    position: absolute;
    left: 150px;
    top: 40px;
    width: 300px;
    height: 690px;
    border-radius: 4px;
    background: linear-gradient(180deg,
      #d9dedb 0%,
      var(--silks) 9%,
      var(--silks-deep) 26%,
      var(--bay) 38%,
      #2a201b 62%,
      #4a3a30 82%,
      rgba(90, 70, 52, 0.85) 100%);
    box-shadow: 0 0 24px rgba(20, 20, 20, 0.35);
  }
  .facets {
    position: absolute;
    inset: 0;
    width: 100%;
    height: 100%;
  }
  .event-mark {
    position: absolute;
    left: 0;
    right: 0;
    top: 352px;
    display: flex;
    justify-content: center;
    align-items: center;
    gap: 10px;
    font-size: 26px;
    letter-spacing: 3px;
    text-shadow: 1px 2px 3px var(--text-shadow);
  }
  .event-mark .mark-dot {
    width: 14px;
    height: 14px;
    border-radius: 50%;
    background: var(--text-light);
  }
  .title-block {
    position: absolute;
    left: 0;
    right: 0;
    text-align: center;
    text-shadow: 2px 3px 4px var(--text-shadow);
  }
  .running {
    top: 428px;
    font-size: 26px;
    letter-spacing: 2px;
  }
  .rule {
    position: absolute;
    left: 67px;
    width: 486px;
    height: 2px;
    background: var(--text-light);
    box-shadow: 1px 2px 3px var(--text-shadow);
  }
  .rule-top { top: 465px; }
  .rule-bottom { top: 602px; }
  .headline {
    top: 466px;
    font-size: 84px;
    font-weight: 700;
    letter-spacing: 3px;
    line-height: 1.05;
  }
  .purse {
    top: 553px;
    font-size: 40px;
    letter-spacing: 1px;
    line-height: 1.1;
  }
  .race-date {
    top: 614px;
    font-size: 27px;
    letter-spacing: 1px;
    line-height: 1.22;
  }
  .host {
    position: absolute;
    left: 0;
    right: 0;
    top: 730px;
    text-align: center;
    text-shadow: 1px 2px 3px var(--text-shadow);
  }
  .host-name {
    font-size: 30px;
    font-weight: 700;
    letter-spacing: 1px;
    line-height: 1;
  }
  .host-tagline {
    margin-top: 8px;
    font-size: 10px;
    letter-spacing: 2px;
  }
  .parent {
    margin-top: 8px;
    display: inline-flex;
    align-items: center;
    gap: 6px;
    font-size: 16px;
    letter-spacing: 1px;
  }
  .parent .parent-square {
    width: 14px;
    height: 14px;
    background: var(--text-light);
  }
</style>
</head>
<body>
  <main class="poster">
    <div class="track-backdrop"></div>
    <div class="race-photo" role="img" aria-label="Jockey in green silks with number 5 riding a dark bay horse straight toward the viewer on a dusty dirt track, another runner blurred behind"></div>

    <svg class="facets" viewBox="0 0 600 844" aria-hidden="true">
      <polygon points="0,0 260,0 0,170" fill="#ffffff" opacity="0.12"/>
      <polygon points="600,0 330,0 600,230" fill="#1c2c3a" opacity="0.12"/>
      <polygon points="0,240 600,110 600,200" fill="#ffffff" opacity="0.08"/>
      <polygon points="0,520 600,420 600,560 0,640" fill="#6f8fa0" opacity="0.18"/>
      <polygon points="0,560 260,700 0,740" fill="#e0a04c" opacity="0.30"/>
      <polygon points="600,620 340,720 600,780" fill="#e0a04c" opacity="0.28"/>
      <polygon points="0,844 600,844 600,760 0,800" fill="#2e2620" opacity="0.35"/>
    </svg>

    <div class="event-mark">
      <span class="mark-dot"></span>
      <span class="mark-name">FALCON CROWN</span>
    </div>

    <p class="title-block running">48TH RUNNING</p>
    <div class="rule rule-top"></div>
    <h1 class="title-block headline">STAKES</h1>
    <p class="title-block purse">$750,000 GRADE III</p>
    <div class="rule rule-bottom"></div>
    <p class="title-block race-date">AUGUST 5, 2017<br>FIRST POST TIME AT 2PM</p>

    <div class="host">
      <p class="host-name">RIDGECREST CASINO</p>
      <p class="host-tagline">RACETRACK &amp; RESORT</p>
      <p class="parent"><span class="parent-square"></span><span>GOLDVALE RESORTS</span></p>
    </div>
  </main>
</body>
</html>
```